Business Card Design

Hello!
We would like you to design some business cards for us. We will send you a sample of what we have. We want to take out the Tidewell Harbor Logo and add the RZD logo. This is the company that we own and it manages 7 to 8 franchised child care locations called Pebble Grove. So you can make the Pebble Grove a little logo smaller than what it currently is. Currently the back of the card lists the locations but we don't need that as we are adding new locations every few months. We can also add the website address for RZD below the logo if needed. We don't like the current design so please change it up as you like. Please let us know if you have any questions.

Industry/Entity Type

Business

Contact Information for Business Card

See above

Font styles to use
Serif
Sans Serif

Colors

Designer to choose colors to be used in the design.

Requirements
Must have
• Clean crisp look

```html
<!DOCTYPE html>
<html lang="en">
<head>
<meta charset="utf-8">
<title>Pebble Grove Business Card</title>
<link rel="stylesheet" href="https://fonts.googleapis.com/css2?family=Montserrat:wght@700&family=Noto+Sans:wght@400;700&display=swap">
<style>
  :root {
    --page: #ece9e4;
    --card-white: #ffffff;
    --navy: #07508a;
    --orange: #f7a024;
    --brick: #aa343a;
    --brick-dark: #8e262c;
    --ink: #222222;
    --grey: #6b6b6b;
  }
  * { box-sizing: border-box; margin: 0; padding: 0; }
  html, body { width: 1200px; height: 1000px; overflow: hidden; }
  body {
    background: var(--page);
    font-family: "Noto Sans", Arial, sans-serif;
    position: relative;
  }
  .card {
    position: absolute;
    width: 525px;
    height: 300px;
    box-shadow: 0 6px 18px rgba(0,0,0,0.18);
    overflow: hidden;
  }
  .card-front { left: 337px; top: 150px; background: var(--card-white); }
  .card-back { left: 337px; top: 540px; background: var(--brick); }

  .front-shapes { position: absolute; inset: 0; }

  .brand {
    position: absolute;
    right: 36px;
    top: 34px;
    text-align: right;
  }
  .brand-name {
    font-size: 30px;
    font-weight: 400;
    color: var(--brick);
    letter-spacing: 0.5px;
    line-height: 1;
  }
  .brand-tagline {
    margin-top: 6px;
    font-size: 15px;
    color: var(--ink);
    letter-spacing: 0.4px;
  }

  .office {
    position: absolute;
    right: 36px;
    top: 160px;
    text-align: right;
  }
  .office-title {
    font-size: 16px;
    font-weight: 700;
    color: var(--brick);
    margin-bottom: 6px;
  }
  .office-address {
    font-size: 12.5px;
    line-height: 1.35;
    color: var(--grey);
  }

  .person {
    position: absolute;
    left: 34px;
    bottom: 30px;
    color: #ffffff;
  }
  .person-name {
    font-family: "Montserrat", Arial, sans-serif;
    font-weight: 700;
    font-size: 22px;
    letter-spacing: 0.5px;
  }
  .person-role {
    font-size: 14px;
    margin-bottom: 10px;
  }
  .contact-list { list-style: none; font-size: 12px; line-height: 1.5; }
  .contact-list li { display: flex; align-items: center; gap: 8px; }
  .contact-list svg { width: 12px; height: 12px; flex: none; }

  .back-mark {
    position: absolute;
    left: 0; right: 0;
    top: 112px;
    display: flex;
    justify-content: center;
    align-items: center;
    gap: 12px;
  }
  .back-mark-dot {
    width: 26px; height: 26px;
    border-radius: 50%;
    background: var(--orange);
  }
  .back-mark-name {
    font-size: 34px;
    font-weight: 700;
    color: var(--orange);
  }
  .back-shadow {
    position: absolute;
    left: 50%;
    top: 230px;
    width: 180px;
    height: 12px;
    margin-left: -90px;
    border-radius: 50%;
    background: var(--brick-dark);
    filter: blur(4px);
    opacity: 0.8;
  }
</style>
</head>
<body>

<section class="card card-front">
  <svg class="front-shapes" viewBox="0 0 525 300" width="525" height="300" aria-hidden="true">
    <polygon points="0,0 35,0 430,300 0,300" fill="var(--navy)"/>
    <polygon points="35,0 125,0 440,300 425,300" fill="var(--orange)"/>
  </svg>

  <div class="brand">
    <div class="brand-name">Pebble Grove</div>
    <div class="brand-tagline">Educational Child Care</div>
  </div>

  <div class="office">
    <div class="office-title">Management Offices</div>
    <div class="office-address">418 Larkspur Avenue<br>Suite G, Fernwood Hills<br>IL 60000</div>
  </div>

  <div class="person">
    <div class="person-name">NADIA VERHOEK</div>
    <div class="person-role">Academy Owner</div>
    <ul class="contact-list">
      <li>
        <svg viewBox="0 0 12 12"><rect x="0.5" y="2" width="11" height="8" fill="#fff"/><polyline points="0.5,2 6,7 11.5,2" fill="none" stroke="var(--navy)" stroke-width="1"/></svg>
        nadia.verhoek@pebblegrove.net
      </li>
      <li>
        <svg viewBox="0 0 12 12"><path d="M1 4 Q6 0 11 4 L9 5.5 L8 4 L4 4 L3 5.5 Z" fill="#fff"/><rect x="2.5" y="6" width="7" height="5" rx="1" fill="#fff"/></svg>
        555 - 014 - 2270
      </li>
      <li>
        <svg viewBox="0 0 12 12"><circle cx="6" cy="6" r="5" fill="none" stroke="#fff" stroke-width="1.2"/><ellipse cx="6" cy="6" rx="2.2" ry="5" fill="none" stroke="#fff" stroke-width="1"/><line x1="1" y1="6" x2="11" y2="6" stroke="#fff" stroke-width="1"/></svg>
        www.pebblegrove.net
      </li>
    </ul>
  </div>
</section>

<section class="card card-back">
  <div class="back-mark">
    <span class="back-mark-dot"></span>
    <span class="back-mark-name">Pebble Grove</span>
  </div>
  <div class="back-shadow"></div>
</section>

</body>
</html>
```